Design a Site That Says: ‘This is the Next Big Thing in Defense Tech

We are redesigning the Torvik Skyworks website to deliver a bold, high-impact digital experience that convinces on-the-fence investors this is the moment to get involved. The site must feel fast-moving, technology-forward, and unlike anything coming out of traditional aerospace — no more beige PDFs or outdated defense branding. It should reflect the precision, autonomy, and scale of our product without revealing the proprietary details. Through sleek, modern visuals, sharp messaging, and subtle cues of aerospace innovation — airport runways, carbon fiber textures, night imagery, and mission-ready tone — we want to guide the audience toward one powerful conclusion: Torvik Skyworks is building the future of autonomous defense aviation, and the time to invest is now.
✈️ What Is Torvik Skyworks?
Torvik Skyworks is a next-generation autonomous aerial system built for the future of defense. Where legacy drones were designed for one-off missions and slow production pipelines, Torvik is built from the ground up for speed, scalability, and autonomy. Its sleek, tailless design reflects not just a new aircraft, but a new philosophy: one where performance, flexibility, and manufacturing efficiency converge.

This is not another iteration — it’s a complete rethink of how unmanned systems should be built, deployed, and scaled.

🧩 Competitive Discriminators
1. Production-First Philosophy
Most aircraft are built like custom machines. Torvik is different — it’s engineered for rapid production using cutting-edge methods adapted from high-rate industries. This isn’t just about speed — it’s about being able to respond to demand in real time.

2. Autonomy at the Core
Torvik doesn’t rely on ground crews or remote pilots. It’s built for full autonomy — to operate as a single asset or as part of a larger, coordinated swarm without micromanagement.

3. Modularity Without Compromise
One airframe. Many missions. With a modular internal architecture, Torvik can be adapted to a wide range of operational roles without altering its core structure — or its production rhythm.

4. Clean Configuration, Internal Systems
Everything is housed inside — systems, sensors, payloads — resulting in a streamlined platform that looks and performs differently from the start.

5. Distinct Visual Signature
From its tailless form to its smooth composite surfaces, Torvik Skyworks looks like the future — because it is. It’s what happens when aerospace engineers design without compromise.

👀 What Will Stand Out — Even to a Casual Observer
It doesn’t look like any drone they’ve seen before.
No tail, no hardpoints, no draggy silhouettes — just smooth geometry and silent confidence.

It feels like it belongs to the next generation.
While legacy platforms show their age, Torvik shows what’s next. It looks engineered, not assembled.

It invites imagination.
Observers can’t help but wonder: What’s inside? What can it do? How is it built so differently?

It feels like a system, not just an aircraft.
From design to production to deployment, everything about Torvik is intentional — and scalable.

```html
<!DOCTYPE html>
<html lang="en">
<head>
<meta charset="utf-8">
<title>Torvik Skyworks</title>
<link rel="stylesheet" href="https://fonts.googleapis.com/css2?family=Barlow:wght@400;500;600&family=Barlow+Condensed:wght@300;400;500;600&display=swap">
<style>
:root{
  --navy:#0b3c6b;
  --navy-deep:#0e1e33;
  --ink:#2f2f2f;
  --dark-btn:#2a2a2a;
  --white:#ffffff;
  --text:#222;
  --muted:#555;
}
*{margin:0;padding:0;box-sizing:border-box}
html,body{width:1200px;height:3462px;overflow:hidden}
body{font-family:"Barlow",sans-serif;color:var(--text);background:var(--white);position:relative}
.cond{font-family:"Barlow Condensed",sans-serif}
section{position:absolute;left:0;width:1200px;overflow:hidden}
.abs{position:absolute}
.btn{position:absolute;display:flex;align-items:center;justify-content:center;font-size:13px;font-weight:500;letter-spacing:.3px;border-radius:4px}
.btn-dark{background:var(--dark-btn);color:var(--white)}
.btn-blue{background:var(--navy);color:var(--white)}
.btn-white{background:var(--white);color:var(--ink)}
.wordmark{font-family:"Barlow",sans-serif;font-weight:600;letter-spacing:2px;display:flex;align-items:center;gap:10px}
.wordmark .dot{width:14px;height:14px;border-radius:50%;background:currentColor}

/* hero */
.hero{top:0;height:487px;background:linear-gradient(180deg,#3a4656 0%,#6f7b88 40%,#9aa3ab 70%,#c5c3bd 100%)}
.hero-art{left:0;top:0;width:1200px;height:487px;background:radial-gradient(ellipse at 60% 60%,rgba(40,44,52,.55) 0%,rgba(40,44,52,0) 55%)}
.nav{top:26px;left:169px;width:863px;height:30px;color:var(--white)}
.nav .wordmark{position:absolute;left:0;top:4px;font-size:20px;color:var(--white)}
.nav-links{position:absolute;left:443px;top:7px;display:flex;gap:27px;font-size:13px}
.nav .members{left:698px;top:-4px;width:119px;height:35px;background:#2b2b2b;color:var(--white)}
.search{position:absolute;left:844px;top:3px}
.hero-kicker{left:169px;top:150px;width:500px;font-size:17px;line-height:21px;color:var(--white)}
.hero-title{left:169px;top:207px;font-size:58px;font-weight:600;line-height:62px;color:var(--white)}
.hero-cta{left:169px;top:363px;width:155px;height:36px}

.band{top:487px;height:96px;background:#000;display:flex;align-items:center;justify-content:center}
.band h2{font-size:60px;font-weight:600;color:var(--white);letter-spacing:.5px}

/* focuses */
.focus{top:583px;height:791px;background:linear-gradient(180deg,#f7f9fb 0%,#e7edf3 55%,#f2f4f6 100%)}
.focus-mark{left:169px;top:150px;width:278px;justify-content:center;font-size:34px;color:var(--navy)}
.focus-title{left:159px;top:300px;width:298px;text-align:center;font-size:80px;font-weight:300;line-height:97px;color:var(--ink)}
.focus-cta{left:231px;top:617px;width:155px;height:36px}
.cards{left:491px;top:88px;width:537px}
.fcard{position:relative;height:87px;margin-bottom:18px;background:var(--navy);border-radius:6px;color:var(--white);display:flex;align-items:center}
.fcard svg{position:absolute;left:18px;top:17px}
.fcard p{margin-left:88px;margin-right:18px;font-size:12.5px;line-height:17px}
.fcard b{font-weight:600}

/* about */
.about{top:1374px;height:462px;background:linear-gradient(180deg,#eef1f5 0%,#f5f6f8 60%,#e8eaee 100%)}
.about-left{left:0;top:0;width:260px;height:462px;background:linear-gradient(100deg,#6f7378 0%,#c9ccd0 60%,rgba(240,242,245,0) 100%)}
.about-right{left:940px;top:200px;width:260px;height:262px;background:linear-gradient(250deg,#7a7e83 0%,#cfd2d6 55%,rgba(240,242,245,0) 100%)}
.about-panel{left:169px;top:90px;width:490px;height:280px;background:rgba(255,255,255,.55);border-radius:8px}
.about h2{position:absolute;left:187px;top:118px;font-size:39px;font-weight:500;color:var(--ink);display:flex;align-items:center;gap:12px}
.about h2 .dot{width:14px;height:14px;border-radius:50%;background:var(--navy)}
.about h2 em{font-style:normal;color:var(--navy)}
.about-copy{left:187px;top:190px;width:470px;font-size:13px;line-height:19.5px;color:var(--ink)}
.about-cta{left:187px;top:311px;width:128px;height:35px}
.plane{left:700px;top:150px;width:170px;height:150px;border-radius:50%;background:radial-gradient(circle,#d9b3ad 0%,rgba(217,179,173,0) 70%)}

/* mission vision */
.mv{top:1836px;height:672px;background:linear-gradient(180deg,#e4e9ee 0%,#eef1f4 100%)}
.mvcard{position:absolute;top:88px;height:496px;background:var(--white);border-radius:8px;overflow:hidden}
.mvcard .img{height:281px}
.mvcard h3{position:absolute;left:18px;top:302px;font-size:28px;font-weight:500;color:var(--text);display:flex;align-items:center;gap:10px}
.mvcard h3 .dot{width:12px;height:12px;border-radius:50%;background:var(--navy)}
.mvcard p{position:absolute;left:18px;top:360px;width:385px;font-size:15px;line-height:20px;color:var(--text)}
.mvcard .btn{left:18px;top:436px;width:104px;height:34px}

/* blogs */
.blogs{top:2508px;height:700px;background:linear-gradient(180deg,#7fb4d9 0%,#a9cfe8 45%,#d7e7f2 100%)}
.blogs h2{position:absolute;left:169px;top:80px;font-size:40px;font-weight:500;color:var(--navy);display:flex;align-items:center;gap:12px}
.blogs h2 .dot{width:14px;height:14px;border-radius:50%;background:var(--navy)}
.blogs .top-btn{left:927px;top:80px;width:104px;height:35px}
.bcard{position:absolute;background:var(--white);border-radius:10px;overflow:hidden}
.feature{left:169px;top:147px;width:347px;height:400px}
.feature .img{position:relative;height:228px;background:linear-gradient(180deg,#0f1a2c 0%,#2a3e5c 55%,#0e1626 100%);border-radius:10px;color:var(--white);font-size:14px}
.feature .img span{position:absolute}
.meta{font-size:11px;color:var(--muted)}
.btitle{font-family:"Barlow Condensed",sans-serif;font-size:19px;font-weight:500;color:var(--navy);margin-top:6px}
.bexcerpt{font-size:11.5px;line-height:15px;color:var(--text);margin-top:8px}
.more{font-size:11px;color:var(--navy);margin-top:8px;font-weight:500}
.feature .body{padding:16px 18px}
.side{left:535px;width:497px;height:190px;display:flex}
.side .img{width:248px;height:190px;flex:none}
.side .body{padding:22px 18px}

/* footer */
.footer{top:3132px;height:330px;background:transparent}
.footer-bg{left:0;top:0}
.foot-mark{left:169px;top:120px;font-size:24px;color:var(--white)}
.socials{left:182px;top:200px;display:flex;gap:14px}
.socials span{width:27px;height:27px;border-radius:50%;background:var(--white);display:flex;align-items:center;justify-content:center}
.foot-col{top:115px;color:var(--white)}
.foot-col h4{font-family:"Barlow Condensed",sans-serif;font-size:24px;font-weight:500;margin-bottom:16px}
.foot-col ul{list-style:none;font-size:13px;line-height:28px;color:#d6dde6}
.contact-row{display:flex;gap:12px;align-items:flex-start;font-size:13px;line-height:19px;color:#d6dde6;margin-bottom:18px}
.contact-row .ic{width:24px;height:24px;border-radius:50%;background:var(--white);flex:none;display:flex;align-items:center;justify-content:center}
</style>
</head>
<body>

<section class="hero">
  <div class="abs hero-art" role="img" aria-label="Tailless autonomous aircraft flying above dramatic clouds"></div>
  <div class="abs nav">
    <div class="wordmark">TORVIK SKYWORKS</div>
    <div class="nav-links"><span>Home</span><span>About</span><span>Contact</span><span>Blog</span></div>
    <div class="btn members">Members Area</div>
    <svg class="search" width="20" height="20" viewBox="0 0 20 20"><circle cx="8" cy="8" r="6" fill="none" stroke="#fff" stroke-width="2"/><line x1="12.5" y1="12.5" x2="18" y2="18" stroke="#fff" stroke-width="2"/></svg>
  </div>
  <p class="abs hero-kicker">Enhancing Warfighter Capability, Driving Affordability, Powering Scalable Innovation</p>
  <h1 class="abs hero-title cond">Revolutionary Capability,<br>Evolutionary Technology</h1>
  <div class="btn btn-white hero-cta">EXPLORE MORE</div>
</section>

<section class="band"><h2 class="cond">BUILT | DEPLOYED | SCALED</h2></section>

<section class="focus">
  <div class="abs wordmark focus-mark"><span class="dot"></span>TORVIK</div>
  <h2 class="abs focus-title cond">Strategic Innovation Focuses</h2>
  <div class="btn btn-dark focus-cta">EXPLORE MORE</div>
  <div class="abs cards">
    <div class="fcard"><svg width="54" height="54" viewBox="0 0 54 54"><circle cx="27" cy="27" r="25" fill="none" stroke="#fff" stroke-width="1.5"/><rect x="18" y="20" width="18" height="14" fill="none" stroke="#fff" stroke-width="1.5"/></svg><p><b>Rapid Airframes</b>: Torvik Skyworks is revolutionizing composite production for aerospace structures by cutting fabrication and assembly times, minimizing labor,</p></div>
    <div class="fcard"><svg width="54" height="54" viewBox="0 0 54 54"><circle cx="27" cy="27" r="25" fill="none" stroke="#fff" stroke-width="1.5"/><circle cx="27" cy="27" r="8" fill="none" stroke="#fff" stroke-width="1.5"/></svg><p><b>Avionics Architecture</b>: We are optimizing the avionics architecture by streamlining its complexity, developing a modular, product-agnostic computing framework with integrated redundancy</p></div>
    <div class="fcard"><svg width="54" height="54" viewBox="0 0 54 54"><circle cx="27" cy="27" r="25" fill="none" stroke="#fff" stroke-width="1.5"/><circle cx="27" cy="27" r="11" fill="none" stroke="#fff" stroke-width="1.5"/><circle cx="27" cy="27" r="4" fill="#fff"/></svg><p><b>Attritable Propulsion</b>: We are developing a high-performance class of engine systems that are manufacturable, easily swappable, and designed for streamlined maintenance</p></div>
    <div class="fcard"><svg width="54" height="54" viewBox="0 0 54 54"><circle cx="27" cy="27" r="25" fill="none" stroke="#fff" stroke-width="1.5"/><rect x="20" y="20" width="14" height="14" fill="none" stroke="#fff" stroke-width="1.5"/><path d="M27 14v6M27 34v6M14 27h6M34 27h6" stroke="#fff" stroke-width="1.5"/></svg><p><b>Artificial Intelligence</b>: We are developing a high-performance class of engine systems that are manufacturable, easily swappable, and designed for streamlined maintenance</p></div>
    <div class="fcard"><svg width="54" height="54" viewBox="0 0 54 54"><circle cx="27" cy="27" r="25" fill="none" stroke="#fff" stroke-width="1.5"/><path d="M14 31L27 21L40 31L27 28Z" fill="none" stroke="#fff" stroke-width="1.5"/></svg><p><b>Spiral Development Aircraft</b>: We are developing a high-performance class of engine systems that are manufacturable, easily swappable, and designed for streamlined maintenance</p></div>
    <div class="fcard"><svg width="54" height="54" viewBox="0 0 54 54"><circle cx="27" cy="27" r="25" fill="none" stroke="#fff" stroke-width="1.5"/><rect x="19" y="22" width="16" height="12" rx="3" fill="none" stroke="#fff" stroke-width="1.5"/><circle cx="23" cy="36" r="2" fill="#fff"/><circle cx="31" cy="36" r="2" fill="#fff"/></svg><p><b>Automated Ground Operations</b>: We are developing a high-performance class of engine systems that are manufacturable, easily swappable, and designed for streamlined maintenance</p></div>
  </div>
</section>

<section class="about">
  <div class="abs about-left" role="img" aria-label="Curved terminal roof structure seen from below"></div>
  <div class="abs about-right" role="img" aria-label="Curved terminal roof structure seen from below"></div>
  <div class="abs plane" role="img" aria-label="Passenger jet flying overhead"></div>
  <div class="abs about-panel"></div>
  <h2 class="cond"><span class="dot"></span>About <em>TORVIK SKYWORKS</em></h2>
  <p class="abs about-copy">Torvik Skyworks, a visionary aerospace engineering firm, was established in 2024 with a core focus on integrating state-of-the-art technologies into Unmanned Aerial Systems (UAS). Our commitment to seamless adoption of cutting-edge advancements distinguishes us, catering to aircraft enthusiasts, aerospace defense, and engineering professionals.</p>
  <div class="btn btn-blue about-cta">EXPLORE MORE</div>
</section>

<section class="mv">
  <div class="mvcard" style="left:169px;width:422px">
    <div class="img" role="img" aria-label="Aircraft over a glowing blue circuit board with electronic components" style="background:linear-gradient(160deg,#2c3a48 0%,#1f6fa8 50%,#3b2c26 100%)"></div>
    <h3 class="cond"><span class="dot"></span>Mission</h3>
    <p>Torvik Skyworks is revolutionizing the aerospace industry with fully autonomous aerial vehicles, seamlessly integrating proven technologies</p>
    <div class="btn btn-dark">READ MORE</div>
  </div>
  <div class="mvcard" style="left:609px;width:424px">
    <div class="img" role="img" aria-label="Engineer overlooking an aircraft production hangar" style="background:linear-gradient(160deg,#8fa3b8 0%,#4a6078 50%,#1d3350 100%)"></div>
    <h3 class="cond"><span class="dot"></span>Vision</h3>
    <p>To transform the aerospace industry by harnessing the best innovations and maximizing every dollar to shape a future where aerospace is defined</p>
    <div class="btn btn-dark">READ MORE</div>
  </div>
</section>

<section class="blogs">
  <h2 class="cond"><span class="dot"></span>Our Blogs</h2>
  <div class="btn btn-dark top-btn">READ MORE</div>
  <div class="bcard feature">
    <div class="img" role="img" aria-label="Tailless aircraft diagram with system areas labelled">
      <span style="left:31px;top:12px">Powerplant</span><span style="right:44px;top:12px">Fluids</span>
      <span style="left:25px;top:176px">Harnessing</span><span style="right:34px;top:176px">Avionics</span>
      <span style="left:120px;top:202px">Ground Support</span>
    </div>
    <div class="body">
      <div class="meta">Dana Whitlock</div>
      <div class="btitle">Where It All Begins</div>
      <div class="bexcerpt">After a short break, we're back with another installment of the Torvik Skyworks blog series, diving deeper into the new space approach</div>
      <div class="more">- Read More</div>
    </div>
  </div>
  <div class="bcard side" style="top:147px">
    <div class="img" role="img" aria-label="Engineer standing beside a large rocket stage in a hangar" style="background:linear-gradient(160deg,#6e6a5e 0%,#9a9486 50%,#cfcac0 100%)"></div>
    <div class="body">
      <div class="meta">Dana Whitlock</div>
      <div class="btitle">Why I Believe I Can</div>
      <div class="bexcerpt">This is my story, about how a kid with the "Knack" that wanted to work on cars, sent something to space, the moon, and is now taking on Aerospace.</div>
      <div class="more">- Read More</div>
    </div>
  </div>
  <div class="bcard side" style="top:357px">
    <div class="img" role="img" aria-label="Autonomous aircraft flying above clouds" style="background:linear-gradient(160deg,#c9d7e3 0%,#7f9bb5 55%,#e4e9ee 100%)"></div>
    <div class="body">
      <div class="meta">Dana Whitlock</div>
      <div class="btitle">Introducing Torvik Skyworks</div>
      <div class="bexcerpt">Torvik Skyworks is an aerospace technology company dedicated to transforming how aerospace innovation happens.</div>
      <div class="more">- Read More</div>
    </div>
  </div>
</section>

<section class="footer">
  <svg class="abs footer-bg" width="1200" height="330" viewBox="0 0 1200 330"><path d="M0 70 Q600 -10 1200 70 L1200 330 L0 330 Z" fill="#0e1e33"/></svg>
  <div class="abs wordmark foot-mark">TORVIK SKYWORKS</div>
  <div class="abs socials">
    <span aria-label="Share"><svg width="13" height="13" viewBox="0 0 13 13"><circle cx="3" cy="6.5" r="1.8" fill="#0e1e33"/><circle cx="10" cy="2.5" r="1.8" fill="#0e1e33"/><circle cx="10" cy="10.5" r="1.8" fill="#0e1e33"/><path d="M3 6.5L10 2.5M3 6.5L10 10.5" stroke="#0e1e33" stroke-width="1.2"/></svg></span>
    <span aria-label="Website"><svg width="13" height="13" viewBox="0 0 13 13"><circle cx="6.5" cy="6.5" r="5.5" fill="none" stroke="#0e1e33" stroke-width="1.2"/><ellipse cx="6.5" cy="6.5" rx="2.3" ry="5.5" fill="none" stroke="#0e1e33" stroke-width="1"/><path d="M1 6.5h11" stroke="#0e1e33" stroke-width="1"/></svg></span>
    <span aria-label="Messages"><svg width="13" height="13" viewBox="0 0 13 13"><path d="M1.5 2h10v7H5l-3 2.5V9h-.5Z" fill="none" stroke="#0e1e33" stroke-width="1.2" stroke-linejoin="round"/></svg></span>
  </div>
  <div class="abs foot-col" style="left:485px">
    <h4>Quick Links</h4>
    <ul><li>Home</li><li>About</li><li>Contact</li><li>Blog</li><li>Members Area</li></ul>
  </div>
  <div class="abs foot-col" style="left:755px;width:280px">
    <h4>Contact</h4>
    <div class="contact-row"><span class="ic"><svg width="12" height="10" viewBox="0 0 12 10"><rect x="0.5" y="0.5" width="11" height="9" fill="none" stroke="#0e1e33"/><path d="M0.5 0.5L6 5L11.5 0.5" fill="none" stroke="#0e1e33"/></svg></span><span>info@torvikskyworks.com</span></div>
    <div class="contact-row"><span class="ic" style="margin-top:12px"><svg width="10" height="13" viewBox="0 0 10 13"><path d="M5 12C5 12 1 7 1 4.5A4 4 0 0 1 9 4.5C9 7 5 12 5 12Z" fill="#0e1e33"/><circle cx="5" cy="4.5" r="1.5" fill="#fff"/></svg></span><span>Torvik Skyworks Inc.<br>4820 Harlow Ridge Drive, Austin, Texas 78730</span></div>
  </div>
</section>

</body>
</html>
```